Design Android App for Creating Estimates and Invoices

This project is to create a graphic design for an Android mobile app called Velmira Builder App which is an app that will help contractors to quickly create professional estimates and invoices, accept payments, manage clients and projects and run their business smoothly.

Link to some designs I created myself, hoping to get even better design from you
https://snapvault.example/album/qTrWpe

This project is similar to
https://appmarket.example/store/apps/details?id=com.brevlo.android.brevlo
https://appmarket.example/store/apps/details?id=com.tuvrq.quikbill

Check this Google Doc for more information. http://shrtn.example/8KmPqX4

Target Market(s)

Contractors, Home Improvement Professionals, Home Builders,

Industry/Entity Type

Residential Construction

Requirements
Must have
• Non-cluttered screen for Estimates, Enough white space between fields.
Nice to have
• Be different from the two example designs shown

```html
<!DOCTYPE html>
<html lang="en">
<head>
<meta charset="utf-8">
<title>Velmira Builder App – Screens</title>
<link rel="stylesheet" href="https://fonts.googleapis.com/css2?family=Poppins:wght@300;400;500&display=swap">
<style>
:root{
  --bg:#3f60a8;
  --brand:#2f56a2;
  --brand-dark:#27498c;
  --white:#ffffff;
  --ink:#1f2430;
  --muted:#8a8f99;
  --line:#e7e9ee;
  --soft:#f4f5f7;
  --orange:#f7740f;
  --paid:#6bd07c;
  --sent:#2f56a2;
  --label:#e8eefb;
  --link:#2f56a2;
}
*{box-sizing:border-box;margin:0;padding:0}
html,body{width:1200px;height:1200px;overflow:hidden}
body{background:var(--bg);font-family:"Poppins",sans-serif;color:var(--ink);position:relative}
.screen{position:absolute;background:var(--white);border-radius:26px;overflow:hidden}
.status{position:absolute;top:8px;left:20px;right:16px;display:flex;justify-content:space-between;font-size:11px;color:var(--white);font-weight:500}
.status svg{height:9px}
.section-label{position:absolute;color:var(--label);font-size:26px;font-weight:300;transform:rotate(-90deg);transform-origin:left top;white-space:nowrap}
.divider{position:absolute;width:1px;background:rgba(255,255,255,.25)}

/* list view */
.list{left:94px;top:34px;width:248px;height:538px}
.list .head{background:var(--brand);height:104px;position:relative;color:var(--white)}
.brand{position:absolute;top:44px;left:10px;display:flex;align-items:center;gap:8px;font-size:13px;font-weight:500;letter-spacing:.3px}
.brand i{width:20px;height:20px;border-radius:50%;background:var(--white);display:block}
.search{position:absolute;top:45px;right:10px}
.tabs{position:absolute;bottom:0;left:0;right:0;display:flex;font-size:10px}
.tabs span{flex:1;text-align:center;padding-bottom:8px;opacity:.7}
.tabs span.on{opacity:1;border-bottom:2px solid var(--white);margin:0 14px}
.viewall{height:30px;background:var(--soft);font-size:9px;color:var(--muted);text-align:right;padding:8px 12px}
.inv{height:66px;margin:0 10px;border-bottom:1px solid var(--line);position:relative;font-size:10.5px}
.inv .t{position:absolute;top:12px;left:1px;font-weight:500}
.inv .a{position:absolute;top:12px;right:1px;font-weight:500}
.inv .n{position:absolute;top:32px;left:1px;font-size:8.5px;color:var(--muted)}
.inv .d{position:absolute;top:46px;left:1px;font-size:8.5px;color:var(--muted)}
.tag{position:absolute;top:44px;right:1px;width:60px;height:13px;border-radius:7px;border:1px solid;font-size:8.5px;text-align:center;line-height:11px}
.tag.paid{color:var(--paid);border-color:var(--paid)}
.tag.sent{color:var(--sent);border-color:var(--sent)}
.tag.over{color:var(--orange);border-color:var(--orange)}
.fab{position:absolute;left:274px;top:0;width:40px;height:40px;border-radius:50%;background:var(--orange)}
.list .fab{left:218px;top:430px;display:flex;align-items:center;justify-content:center;color:var(--white);font-size:24px;font-weight:300;box-shadow:0 3px 8px rgba(247,116,15,.4)}
.nav{position:absolute;left:0;right:0;bottom:0;height:70px;background:var(--white);border-top:1px solid var(--line);display:flex;padding-top:10px}
.nav div{flex:1;text-align:center;font-size:7.5px;color:var(--muted)}
.nav div.on{color:var(--brand)}
.nav svg{display:block;margin:0 auto 3px}
.home-bar{position:absolute;bottom:8px;left:50%;transform:translateX(-50%);width:90px;height:3px;border-radius:2px;background:#c9ccd3}

/* walkthrough */
.walk{left:94px;top:627px;width:248px;height:538px;background:var(--brand)}
.skip{position:absolute;top:44px;right:14px;font-size:11px;color:var(--white)}
.art{position:absolute;left:40px;top:110px;width:178px;height:145px;border-radius:60px 70px 50px 80px;background:linear-gradient(160deg,#4f70b6,#3a5ea8)}
.dots{position:absolute;top:305px;left:0;right:0;display:flex;justify-content:center;gap:6px}
.dots i{width:5px;height:5px;border-radius:50%;background:#7e98cc}
.dots i.on{background:var(--white)}
.walk h2{position:absolute;top:332px;left:0;right:0;text-align:center;color:var(--white);font-size:16px;font-weight:500}
.walk p{position:absolute;top:372px;left:20px;right:20px;text-align:center;color:var(--white);font-size:11px;line-height:17px;font-weight:300}
.walk .home-bar{background:rgba(255,255,255,.6)}

/* estimate */
.est{left:533px;top:37px;width:298px;height:712px;background:var(--soft)}
.est2{left:902px;top:43px;width:248px;height:538px;background:var(--soft)}
.ehead{background:var(--brand);height:98px;position:relative;color:var(--white)}
.ehead h1{position:absolute;bottom:26px;left:0;right:0;text-align:center;font-size:17px;font-weight:400}
.ehead svg{position:absolute;left:14px;bottom:30px}
.est2 .ehead{height:81px}
.est2 .ehead h1{font-size:14px;bottom:20px}
.est2 .ehead svg{left:12px;bottom:22px}
.block{background:var(--white);padding:0 14px;margin-bottom:6px}
.row{display:flex;justify-content:space-between;align-items:center;font-size:13px}
.plus{width:19px;height:19px;border-radius:50%;background:var(--orange);color:var(--white);font-size:15px;line-height:19px;text-align:center}
.cap{font-size:11px;color:var(--muted);padding:14px 0 10px;border-bottom:1px solid var(--line)}
.sum .row{color:var(--muted);height:28px}
.sum .row b{font-weight:400;color:var(--ink)}
.link{color:var(--link)}
.small{font-size:10px;color:var(--muted)}
.est2 .row{font-size:11px}
.est2 .cap{font-size:9px;padding:12px 0 8px}
.btn{display:block;margin:30px auto 0;width:178px;height:35px;border-radius:3px;background:var(--brand);color:var(--white);font-size:12px;text-align:center;line-height:35px}
</style>
</head>
<body>

<!-- list view -->
<section class="screen list">
  <div class="head">
    <div class="status"><span>9:41</span><svg viewBox="0 0 50 10" width="50"><rect x="0" y="6" width="2" height="4" fill="#fff"/><rect x="3" y="4" width="2" height="6" fill="#fff"/><rect x="6" y="2" width="2" height="8" fill="#fff"/><rect x="9" y="0" width="2" height="10" fill="#fff"/><path d="M18 4q5-4 10 0M20 6q3-2 6 0" stroke="#fff" fill="none" stroke-width="1.4"/><rect x="34" y="1" width="14" height="8" rx="2" fill="#fff"/></svg></div>
    <div class="brand"><i></i>VELMIRA</div>
    <svg class="search" width="14" height="14" viewBox="0 0 14 14"><circle cx="6" cy="6" r="4.5" stroke="#fff" stroke-width="1.5" fill="none"/><path d="M9.5 9.5l3.5 3.5" stroke="#fff" stroke-width="1.5"/></svg>
    <div class="tabs"><span class="on">INVOICES</span><span>ESTIMATES</span></div>
  </div>
  <div class="viewall">View all ▾</div>
  <div class="inv"><span class="t">Carpenter Work</span><span class="a">$105.00</span><span class="n">INV005</span><span class="d">Jul, 3 2019</span><span class="tag paid">Paid</span></div>
  <div class="inv"><span class="t">Carpenter Work</span><span class="a">$105.00</span><span class="n">INV005</span><span class="d">Jul, 3 2019</span><span class="tag sent">Sent</span></div>
  <div class="inv"><span class="t">Carpenter Work</span><span class="a">$105.00</span><span class="n">INV005</span><span class="d">Jul, 3 2019</span><span class="tag over">Overdue</span></div>
  <div class="inv"><span class="t">Carpenter Work</span><span class="a">$105.00</span><span class="n">INV005</span><span class="d">Jul, 3 2019</span><span class="tag paid">Paid</span></div>
  <div class="inv"><span class="t">Carpenter Work</span><span class="a">$105.00</span><span class="n">INV005</span><span class="d">Jul, 3 2019</span><span class="tag paid">Paid</span></div>
  <div class="fab">+</div>
  <nav class="nav">
    <div class="on"><svg width="16" height="14" viewBox="0 0 16 14"><path d="M0 2h2M4 2h12M0 7h2M4 7h12M0 12h2M4 12h12" stroke="currentColor" stroke-width="1.6"/></svg>Home</div>
    <div><svg width="18" height="16" viewBox="0 0 18 16"><path d="M1 5l8-4 8 4v7l-8 4-8-4z" fill="#9aa0ab"/></svg>Home</div>
    <div><svg width="16" height="16" viewBox="0 0 16 16"><circle cx="8" cy="4.5" r="3.8" fill="#9aa0ab"/><path d="M1 16q0-7 7-7t7 7z" fill="#9aa0ab"/></svg>Home</div>
    <div><svg width="16" height="16" viewBox="0 0 16 16"><circle cx="8" cy="8" r="5.5" fill="none" stroke="#9aa0ab" stroke-width="3" stroke-dasharray="2.5 1.8"/><circle cx="8" cy="8" r="2.5" fill="#9aa0ab"/></svg>Home</div>
  </nav>
  <div class="home-bar"></div>
</section>
<div class="divider" style="left:384px;top:280px;height:230px"></div>
<div class="section-label" style="left:398px;top:455px">List View</div>

<!-- walkthrough -->
<section class="screen walk">
  <div class="status"><span>9:41</span><svg viewBox="0 0 50 10" width="50"><rect x="0" y="6" width="2" height="4" fill="#fff"/><rect x="3" y="4" width="2" height="6" fill="#fff"/><rect x="6" y="2" width="2" height="8" fill="#fff"/><rect x="9" y="0" width="2" height="10" fill="#fff"/><path d="M18 4q5-4 10 0M20 6q3-2 6 0" stroke="#fff" fill="none" stroke-width="1.4"/><rect x="34" y="1" width="14" height="8" rx="2" fill="#fff"/></svg></div>
  <div class="skip">Skip</div>
  <div class="art" role="img" aria-label="Illustration of a paper invoice receipt with an orange check mark"></div>
  <div class="dots"><i class="on"></i><i></i><i></i></div>
  <h2>Easy Invoice</h2>
  <p>Lorem Ipsum is simply dummy text of the printing and typesetting industry. Lorem Ipsum has been the</p>
  <div class="home-bar"></div>
</section>
<div class="divider" style="left:384px;top:750px;height:240px"></div>
<div class="section-label" style="left:398px;top:960px">Walkthrough</div>

<!-- create estimate -->
<section class="screen est">
  <div class="ehead">
    <div class="status" style="top:14px;font-size:13px"><span>9:41</span><svg viewBox="0 0 50 10" width="56" style="height:10px"><rect x="0" y="6" width="2" height="4" fill="#fff"/><rect x="3" y="4" width="2" height="6" fill="#fff"/><rect x="6" y="2" width="2" height="8" fill="#fff"/><rect x="9" y="0" width="2" height="10" fill="#fff"/><path d="M18 4q5-4 10 0M20 6q3-2 6 0" stroke="#fff" fill="none" stroke-width="1.4"/><rect x="34" y="1" width="14" height="8" rx="2" fill="#fff"/></svg></div>
    <svg width="10" height="18" viewBox="0 0 10 18"><path d="M9 1L1 9l8 8" stroke="#fff" stroke-width="1.8" fill="none"/></svg>
    <h1>Create Estimate</h1>
  </div>
  <div class="block" style="padding-top:24px;padding-bottom:20px">
    <div class="row" style="height:18px"><span>Description</span><span class="plus">+</span></div>
    <div class="row" style="height:18px;margin-top:24px"><span>Client</span><span class="plus">+</span></div>
  </div>
  <div class="block" style="padding-bottom:20px">
    <div class="cap">Items</div>
    <div class="row" style="margin-top:20px"><span>Add Item</span><span>$0.00</span></div>
    <div class="small" style="margin-top:4px;font-size:11px">1.00 x $0.00</div>
  </div>
  <div class="block sum" style="padding:12px 14px">
    <div class="row"><span>Subtotal</span><b>$0.00</b></div>
    <div class="row"><span>Discount</span><span class="link">Add</span></div>
    <div class="row"><span>Tax (0.00%)</span><b>$0.00</b></div>
    <div class="row"><span>Total</span><b>$0.00</b></div>
  </div>
  <div class="block" style="padding-top:18px;height:186px">
    <div class="row"><span>Payment Details</span><span class="link">Add</span></div>
    <div class="row" style="margin-top:14px;padding-bottom:10px;border-bottom:1px solid var(--line)"><span>Notes</span></div>
    <div class="small" style="margin-top:12px;font-size:11px">Add Notes</div>
    <div class="row" style="margin-top:72px"><span>Photos <span class="small">(Max 5)</span></span></div>
  </div>
  <div class="home-bar" style="width:108px"></div>
</section>
<div class="divider" style="left:605px;top:770px;height:220px"></div>
<div class="section-label" style="left:620px;top:962px">Estimate</div>

<!-- create estimate, lower part -->
<section class="screen est2">
  <div class="ehead">
    <div class="status"><span>9:41</span><svg viewBox="0 0 50 10" width="50"><rect x="0" y="6" width="2" height="4" fill="#fff"/><rect x="3" y="4" width="2" height="6" fill="#fff"/><rect x="6" y="2" width="2" height="8" fill="#fff"/><rect x="9" y="0" width="2" height="10" fill="#fff"/><path d="M18 4q5-4 10 0M20 6q3-2 6 0" stroke="#fff" fill="none" stroke-width="1.4"/><rect x="34" y="1" width="14" height="8" rx="2" fill="#fff"/></svg></div>
    <svg width="9" height="16" viewBox="0 0 10 18"><path d="M9 1L1 9l8 8" stroke="#fff" stroke-width="1.8" fill="none"/></svg>
    <h1>Create Estimate</h1>
  </div>
  <div class="block" style="padding:16px 10px 12px">
    <div class="row" style="padding-bottom:8px;border-bottom:1px solid var(--line)"><span>Photos <span class="small">(Max 5)</span></span></div>
    <div style="display:flex;gap:9px;margin-top:9px">
      <div role="img" aria-label="Thumbnail of an attached document photo" style="width:29px;height:29px;border:1px solid #c9ccd3;background:linear-gradient(#f2f4f8,#dfe4ec)"></div>
      <div style="width:29px;height:29px;border:1px solid #9aa0ab;text-align:center;line-height:27px;color:var(--muted);font-size:13px">+</div>
    </div>
  </div>
  <div class="block" style="padding:0 10px 12px">
    <div class="cap">Contract and Signature</div>
    <div class="row" style="margin-top:14px"><span>Company Signature</span><span class="link">Add</span></div>
    <div class="row" style="margin-top:7px"><span>Client Signature</span><span class="link">Add</span></div>
  </div>
  <div class="block" style="padding:0 10px 18px">
    <div class="cap">Document Information</div>
    <div class="row" style="margin-top:14px"><span class="small" style="font-size:11px">Estimate #</span><span>EST02</span></div>
    <div class="row" style="margin-top:11px"><span class="small" style="font-size:11px">Date</span><span>12Jan, 2019</span></div>
  </div>
  <div class="block" style="height:110px;padding-top:1px;margin:0"><span class="btn">Create</span></div>
  <div class="home-bar"></div>
</section>
<div class="divider" style="left:948px;top:600px;height:200px"></div>
<div class="section-label" style="left:962px;top:776px">Estimate</div>

</body>
</html>
```